Brantley Advisory Group provides support for renewable energy projects to utilities and suppliers

I need a professional looking business card that is both simple and elegant and unique. My clients are mostly large organizations not individuals. I am a consultant with my own company that is small but would like to give clients the impression I am larger. Smart grid, fiber optics, software, field hardware, distribution automation, substation automation, operations, energy storage/batteries, microgrids, customer service, strategy/roadmaps, conservation, Automated Metering Infrastruture (AMI or smart meters) are all areas of focus.

Target Market(s)

Utilities, suppliers, governmental agencies involved in energy. All types of energy especially natural gas and electrical. Especially renewable energy or green projects.

Contact Information for Business Card

Name - Ross Brantley Cell Phone - 425.318.4762 Email - rbrantley@brantleyag-example.com
Company - Brantley Advisory Group (logo) Title - Principal

Font styles to use
Serif
Sans Serif

Colors

Designer to choose colors to be used in the design.

Requirements
Must have
• Simple and professional and powerful.
• Unique/creative design.
Nice to have
• Utilize color scheme to accent logo colors. Maybe some geometric pattern on edge of card with color.
Should not have
• Busy, complicated, traditional

```html
<!DOCTYPE html>
<html lang="en">
<head>
<meta charset="utf-8">
<title>Brantley Advisory Group – Business Card</title>
<link rel="stylesheet" href="https://fonts.googleapis.com/css2?family=Open+Sans:wght@600;700&family=Libre+Baskerville&display=swap">
<style>
  :root {
    --backdrop: #ece8e1;
    --card-grey: #5e5f63;
    --card-white: #ffffff;
    --brand-blue: #22449a;
    --brand-green: #6a9a3a;
    --text-white: #ffffff;
    --edge-shadow: rgba(0, 0, 0, 0.18);
  }
  * { box-sizing: border-box; margin: 0; padding: 0; }
  html, body {
    width: 1200px;
    height: 902px;
    overflow: hidden;
    background: var(--backdrop);
  }
  .stage {
    position: relative;
    width: 1200px;
    height: 902px;
    display: flex;
    align-items: center;
    justify-content: center;
    gap: 40px;
  }
  .card {
    position: relative;
    width: 540px;
    height: 309px;
    border-radius: 22px;
    overflow: hidden;
    box-shadow: 0 3px 10px var(--edge-shadow);
  }

  /* Back side */
  .card--back {
    background: var(--card-grey);
    display: flex;
    align-items: center;
    justify-content: center;
    gap: 16px;
  }
  .brand-square {
    width: 34px;
    height: 34px;
    border: 3px solid var(--text-white);
    border-radius: 4px;
  }
  .card--back .brand-name {
    font-family: "Open Sans", sans-serif;
    font-weight: 700;
    font-size: 30px;
    color: var(--text-white);
    letter-spacing: 0.2px;
  }

  /* Front side */
  .card--front { background: var(--card-white); }
  .front-brand {
    position: absolute;
    left: 40px;
    top: 62px;
    display: flex;
    align-items: center;
    gap: 12px;
  }
  .front-brand .brand-square {
    width: 26px;
    height: 26px;
    border-color: var(--brand-blue);
  }
  .front-brand .brand-name {
    font-family: "Open Sans", sans-serif;
    font-weight: 700;
    font-size: 21px;
    color: var(--brand-blue);
    line-height: 1.15;
    width: 190px;
  }
  .contact {
    position: absolute;
    right: 26px;
    top: 36px;
    font-family: "Libre Baskerville", serif;
    font-size: 11.5px;
    color: var(--brand-green);
    text-align: right;
    line-height: 1.9;
  }
  .contact-line {
    display: flex;
    align-items: center;
    justify-content: flex-end;
    gap: 8px;
  }
  .contact-icon { width: 13px; height: 13px; flex: none; }
  .accent-band {
    position: absolute;
    left: 0;
    right: 0;
    top: 150px;
    height: 34px;
    background: var(--brand-blue);
  }
  .person {
    position: absolute;
    left: 40px;
    bottom: 30px;
    font-family: "Libre Baskerville", serif;
  }
  .person-name {
    font-size: 20px;
    color: var(--brand-blue);
  }
  .person-title {
    font-size: 14px;
    color: var(--brand-green);
    margin-top: 2px;
  }
</style>
</head>
<body>
<main class="stage">
  <section class="card card--back" aria-label="Card back">
    <span class="brand-square"></span>
    <span class="brand-name">Brantley Advisory Group</span>
  </section>

  <section class="card card--front" aria-label="Card front">
    <div class="front-brand">
      <span class="brand-square"></span>
      <span class="brand-name">Brantley Advisory Group</span>
    </div>

    <div class="contact">
      <div class="contact-line">
        <span>+425.318.4762</span>
        <svg class="contact-icon" viewBox="0 0 16 16" aria-hidden="true">
          <path fill="#22449a" d="M3.2 1.5l2.3 0 1 3.3-1.5 1.1c.8 1.8 2.3 3.3 4.1 4.1l1.1-1.5 3.3 1v2.3c0 .9-.8 1.6-1.7 1.5C6.6 12.8 3.2 9.4 1.7 3.2 1.6 2.3 2.3 1.5 3.2 1.5z"/>
        </svg>
      </div>
      <div class="contact-line">
        <span>rbrantley@brantleyag-example.com</span>
        <svg class="contact-icon" viewBox="0 0 16 16" aria-hidden="true">
          <rect x="1" y="3" width="14" height="10" rx="1" fill="#22449a"/>
          <path d="M1.5 3.8L8 9l6.5-5.2" fill="none" stroke="#ffffff" stroke-width="1.3"/>
        </svg>
      </div>
    </div>

    <div class="accent-band"></div>

    <div class="person">
      <div class="person-name">Ross Brantley</div>
      <div class="person-title">Owner</div>
    </div>
  </section>
</main>
</body>
</html>
```